Bring to life the sophistication and high-level expertise of my consulting business

I am looking for a sleek, modern, sharp PowerPoint design package, with options for a wide range of slide types.
We would like our logo/graphic and its colors (a blue pallet) to be prominently featured. The design should communicate expertise, sophistication, executive-level of work, be bold and look clean and sleek at the same time. There should be no doubt this was professionally done.
The font that will best work with this logo is a basic font using AvantGarde BkBt (custom)
Company briefing:
A consulting and advisory practice specialized in the Consumer Goods and Services Industries. Our methodology is distinguished by its ability to transform visionary thinking—be it blue-sky ideas, inspiration, or innovation—into practical strategies. We drive initiatives aimed at driving revenue growth and enhancing profit margins using 3 pillars: THE PEOPLE, THE CUSTOMER EXPERIENCE and THE OPERATING PLATFORM.
Target audiences are in 3 key areas: C-suite executives (owners and decision-makers of small to mid-cap companies), partners in larger Consulting Companies and Investment Firms (Private Equity/Venture capital, etc)

*In addition to the PowerPoint package, I would like a quote for designs for an email signature, a Microsoft Word template, and a company LinkedIn page (all in the same style as the PPT template)
Updates

Low design quality

Target Market(s)

Target audiences are in 3 key areas: C-suite executives (owners and decision-makers), partners in larger Consulting Companies and Investment Firms (Private Equity/Venture capital, etc.)

Industry/Entity Type

Business Consulting and Advisory

Font styles to use
Sans Serif
Other font styles liked:
• The font that will work best with the logo is basic font using AvantGarde BkBt (custom)

Colors
0054AA
0677BA
7BADD7
CADEEF
E8F1F8
0094D4
00A9DD
6FCCEA
C7EBF8
E9F6FB

Requirements
Must have
• We would like our logo, the graphic shapes and its colors (a blue pallet) to be prominently featured. The design should communicate expertise, sophistication, executive-level of work. It should be sleek, modern, bold and unique.
Nice to have
• A large number of slide options for each type of slide as part of the package
Should not have
• it should not look busy, generic or too traditional

```html
<!DOCTYPE html>
<html lang="en">
<head>
<meta charset="utf-8">
<title>Altavera Presentation Template</title>
<link href="https://fonts.googleapis.com/css2?family=Montserrat:wght@300;400;600;700;800&family=Questrial&display=swap" rel="stylesheet">
<style>
:root{
  --navy:#0054AA;
  --blue:#0677BA;
  --sky:#0094D4;
  --cyan:#00A9DD;
  --aqua:#6FCCEA;
  --pale:#E9F6FB;
  --canvas:#E6F3FB;
  --ink:#1d2530;
  --text:#3a4250;
  --grey:#d9dde2;
  --white:#ffffff;
}
*{margin:0;padding:0;box-sizing:border-box}
html,body{width:1200px;height:4051px;overflow:hidden}
body{background:var(--canvas);font-family:"Questrial",sans-serif;color:var(--text);position:relative}
.slide{position:absolute;left:75px;width:1048px;height:589px;background:linear-gradient(135deg,#ffffff 0%,#f4f7fa 60%,#eef2f6 100%);overflow:hidden;box-shadow:0 2px 10px rgba(0,60,120,.08)}
.abs{position:absolute}
.top-band{position:absolute;left:0;top:0;width:1048px;height:7px;background:var(--grey)}
.top-band::before{content:"";position:absolute;left:0;top:0;width:758px;height:7px;background:var(--navy)}
.slide-title{position:absolute;left:61px;top:34px;font-family:"Montserrat",sans-serif;font-size:29px;font-weight:300;color:var(--ink);letter-spacing:-.5px}
.slide-title b{font-weight:700}
.title-rule{position:absolute;left:0;top:84px;width:120px;height:2px;background:var(--cyan)}
.title-rule::after{content:"";position:absolute;right:-6px;top:-5px;width:12px;height:12px;border-radius:50%;background:var(--sky)}
.brand{position:absolute;right:60px;top:46px;display:flex;align-items:center;gap:8px;font-family:"Questrial",sans-serif;font-size:17px;letter-spacing:.5px;color:var(--navy)}
.brand-dot{width:16px;height:16px;border-radius:50%;background:var(--sky)}
.footer{position:absolute;left:0;top:545px;width:990px;height:34px;border-radius:0 17px 17px 0;background:linear-gradient(90deg,var(--navy),var(--cyan));color:#fff;font-size:11px;display:flex;align-items:center}
.contact{display:flex;align-items:center;gap:12px;margin-left:61px}
.contact + .contact{margin-left:46px}
.contact-icon{width:22px;height:22px;border-radius:50%;background:#fff;display:flex;align-items:center;justify-content:center}
.page-no{margin-left:auto;margin-right:46px;font-family:"Montserrat",sans-serif;font-weight:700;font-size:10px;letter-spacing:1.5px}
.page-no::after{content:"";display:inline-block;width:8px;height:8px;border-radius:50%;background:#fff;margin-left:26px;vertical-align:middle}
.photo{position:absolute;border-radius:14px;overflow:hidden}
.body-copy{font-size:11.6px;line-height:20.5px;text-align:justify;color:var(--text)}
.bullets{list-style:none}
.bullets li{position:relative;padding-left:28px}
.bullets li::before{content:"";position:absolute;left:0;top:4px;width:9px;height:9px;border-radius:50%;border:2px solid var(--sky)}
/* hero */
.hero-photo{position:absolute;left:0;top:0;width:1048px;height:400px}
.hero-brand{position:absolute;left:400px;top:186px;display:flex;align-items:center;gap:14px;font-size:34px;letter-spacing:1px;color:#fff}
.hero-brand .brand-dot{width:30px;height:30px;background:#fff}
.welcome{position:absolute;left:61px;top:436px;font-family:"Montserrat",sans-serif;font-weight:600;font-size:14px;color:var(--blue)}
.hero-name{position:absolute;left:61px;top:457px;font-family:"Montserrat",sans-serif;font-weight:800;font-size:40px;color:var(--ink);letter-spacing:-.5px}
.hero-lead{position:absolute;left:61px;top:514px;width:540px;font-size:13px;line-height:21px;color:var(--text)}
/* about */
.about-title{position:absolute;left:566px;top:118px;font-family:"Montserrat",sans-serif;font-size:40px;font-weight:300;color:var(--ink);letter-spacing:-1px}
.about-title b{font-weight:700}
.about-name{position:absolute;left:566px;top:170px;font-family:"Questrial",sans-serif;font-size:22px;letter-spacing:2px;color:var(--sky)}
.about-copy{position:absolute;left:566px;top:214px;width:422px}
.about-copy p{font-size:11.4px;line-height:19.8px}
.about-copy p + p{margin-top:12px}
/* pillars */
.pillar{position:absolute;width:345px}
.pillar h3,.card h3{font-family:"Montserrat",sans-serif;font-weight:700;font-size:14px;color:var(--ink);margin-bottom:8px}
.pillar p{font-size:11.6px;line-height:18px}
.pillar-icon{position:absolute;width:72px;height:72px;border-radius:50%;background:#fff;box-shadow:0 3px 8px rgba(0,80,160,.2);display:flex;align-items:center;justify-content:center}
.pillar-icon span{width:56px;height:56px;border-radius:50%;display:flex;align-items:center;justify-content:center}
/* focus */
.focus-list li{font-size:12.2px;font-style:italic;font-weight:600;color:var(--ink);line-height:18px;margin-bottom:10px;font-family:"Montserrat",sans-serif}
/* benefits */
.card{position:absolute;top:200px;width:253px;height:231px;border:2px solid var(--sky);border-radius:14px;background:#fff;box-shadow:0 8px 14px rgba(0,90,170,.12);padding:56px 24px 0 24px}
.card p{font-size:11.6px;line-height:18px;color:var(--text)}
.card-icon{position:absolute;left:24px;top:-42px;width:80px;height:80px;border-radius:50%;background:linear-gradient(135deg,var(--navy),var(--cyan));border:5px solid #fff;box-shadow:0 2px 6px rgba(0,80,160,.25);display:flex;align-items:center;justify-content:center}
</style>
</head>
<body>

<!-- Slide 1: Welcome -->
<section class="slide" style="top:88px">
  <svg class="hero-photo" viewBox="0 0 1048 400" role="img" aria-label="Photo of a business team shaking hands in a meeting, blue tinted">
    <defs>
      <linearGradient id="heroTint" x1="0" y1="0" x2="1" y2="1">
        <stop offset="0" stop-color="#2a86c9"/><stop offset=".5" stop-color="#0f6fb2"/><stop offset="1" stop-color="#1c5f9c"/>
      </linearGradient>
    </defs>
    <path d="M0 0H1048V330C900 310 820 400 640 392C420 380 200 330 0 372Z" fill="url(#heroTint)"/>
    <path d="M0 372C200 330 420 380 640 392C820 400 900 310 1048 330V346C900 330 820 412 640 406C420 396 200 350 0 388Z" fill="#c9ced6"/>
  </svg>
  <div class="hero-brand"><span class="brand-dot"></span>Altavera</div>
  <svg class="abs" style="left:647px;top:299px" width="264" height="264" viewBox="0 0 264 264" role="img" aria-label="Portrait photo of the founder">
    <circle cx="132" cy="132" r="130" fill="#fff"/>
    <circle cx="132" cy="132" r="118" fill="#d8d2c8"/>
  </svg>
  <div class="welcome">WELCOME TO</div>
  <div class="hero-name">ALTAVERA</div>
  <p class="hero-lead">Lorem ipsum dolor sit amet, consectetur adipiscing elit, sed do eiusmod tempor incididunt ut labore et dolore magna aliqua.</p>
</section>

<!-- Slide 2: About -->
<section class="slide" style="top:745px">
  <svg class="abs" style="left:0;top:0" width="560" height="545" viewBox="0 0 560 545" role="img" aria-label="Portrait photo of the founder smiling in an office">
    <path d="M0 0H470C560 90 560 320 470 420C400 500 300 530 160 540H0Z" fill="#cfc9c1"/>
  </svg>
  <svg class="abs" style="left:306px;top:318px" width="180" height="180" viewBox="0 0 180 180" aria-hidden="true">
    <defs><linearGradient id="aboutBadge" x1="0" y1="0" x2="1" y2="1"><stop offset="0" stop-color="#0054AA"/><stop offset="1" stop-color="#00A9DD"/></linearGradient></defs>
    <circle cx="90" cy="90" r="88" fill="#fff"/>
    <circle cx="90" cy="90" r="72" fill="url(#aboutBadge)"/>
  </svg>
  <div class="brand"><span class="brand-dot"></span>Altavera</div>
  <h1 class="about-title">ABOUT <b>ME</b></h1>
  <div class="about-name">I'm Marina Castell</div>
  <div class="about-copy body-copy">
    <p>I am a founder/CEO and senior retail executive who manages $1.5B P&amp;Ls and has repeatedly led iconic industry-leading brands – including Maison Lavelle, Hartwell Stores Group, Corvin Footwear, Bayline Hotel and Resorts and the Sunvale Parks Company – to revenue growth, increased market share and operational profitability. As a global customer experience expert, I increase brand recognition, customer retention and loyalty. As a Board member, I can chair committees on strategy, compensation, digital transformation, ESG, risk, governance, and valuation.</p>
    <p>As the Founder and CEO of Altavera, I currently serve as a consultant and advisor collaborating with a diverse array of companies and industries, in addition to serving as a Director on the Brightpath.Org Board and a Strategic Advisor for Northwind Global.</p>
  </div>
  <div class="footer">
    <div class="contact"><span class="contact-icon"><svg width="12" height="12" viewBox="0 0 24 24"><path d="M6.6 10.8a15 15 0 006.6 6.6l2.2-2.2a1 1 0 011-.25 11.4 11.4 0 003.6.57 1 1 0 011 1V20a1 1 0 01-1 1A17 17 0 013 4a1 1 0 011-1h3.5a1 1 0 011 1c0 1.25.2 2.45.57 3.57a1 1 0 01-.25 1z" fill="#0054AA"/></svg></span>+1 (555) 010 2040</div>
    <div class="contact"><span class="contact-icon"><svg width="12" height="12" viewBox="0 0 24 24"><rect x="3" y="6" width="18" height="12" rx="2" fill="#0054AA"/><path d="M3 7l9 6 9-6" stroke="#fff" stroke-width="1.6" fill="none"/></svg></span>info@Altavera.com</div>
    <div class="page-no">PAGE NO 02</div>
  </div>
</section>

<!-- Slide 3: Highlights -->
<section class="slide" style="top:1401px">
  <div class="top-band"></div>
  <h2 class="slide-title">VALUE-CREATION <b>HIGHLIGHTS</b></h2>
  <div class="title-rule"></div>
  <div class="brand"><span class="brand-dot"></span>Altavera</div>
  <ul class="bullets body-copy abs" style="left:61px;top:140px;width:400px">
    <li style="margin-bottom:12px">Double-digit revenue growth and industry leadership by focusing on customer experience, evolving selling and service models, and seamlessly integrating digital and physical channels.</li>
    <li style="margin-bottom:12px">Leads Customer Engagement and CLV double-digit YoY growth in conversion and UPT/AVT by driving complete customer experience overhauls, establishing clienteling foundations and building physical and digital service portfolios</li>
    <li style="margin-bottom:12px">Increased margins and boosted productivity within a 12-month period through business model optimization, team reorganization, enhanced performance, and operational efficiencies.</li>
    <li style="margin-bottom:12px">Market share expansion through strategic planning, refined capital structuring approaches, and effective product and brand positioning/rebranding.</li>
    <li>Development and profitable scaling global operations for IPO readiness by leveraging digital and technology transformations.</li>
  </ul>
  <svg class="photo" style="left:524px;top:129px" width="464" height="382" viewBox="0 0 464 382" role="img" aria-label="Photo of a diverse team talking around a meeting table">
    <defs><linearGradient id="teamPhoto" x1="0" y1="0" x2="0" y2="1"><stop offset="0" stop-color="#e8ecef"/><stop offset="1" stop-color="#8a8580"/></linearGradient></defs>
    <rect width="464" height="382" fill="url(#teamPhoto)"/>
  </svg>
  <div class="footer">
    <div class="contact"><span class="contact-icon"><svg width="12" height="12" viewBox="0 0 24 24"><path d="M6.6 10.8a15 15 0 006.6 6.6l2.2-2.2a1 1 0 011-.25 11.4 11.4 0 003.6.57 1 1 0 011 1V20a1 1 0 01-1 1A17 17 0 013 4a1 1 0 011-1h3.5a1 1 0 011 1c0 1.25.2 2.45.57 3.57a1 1 0 01-.25 1z" fill="#0054AA"/></svg></span>+1 (555) 010 2040</div>
    <div class="contact"><span class="contact-icon"><svg width="12" height="12" viewBox="0 0 24 24"><rect x="3" y="6" width="18" height="12" rx="2" fill="#0054AA"/><path d="M3 7l9 6 9-6" stroke="#fff" stroke-width="1.6" fill="none"/></svg></span>info@Altavera.com</div>
    <div class="page-no">PAGE NO 03</div>
  </div>
</section>

<!-- Slide 4: Pillars -->
<section class="slide" style="top:2059px">
  <div class="top-band"></div>
  <h2 class="slide-title">OUR <b>3 PILLARS</b></h2>
  <div class="title-rule"></div>
  <div class="brand"><span class="brand-dot"></span>Altavera</div>
  <svg class="abs" style="left:82px;top:126px" width="380" height="380" viewBox="0 0 380 380" role="img" aria-label="Photo of hands around coin stacks with growing plants and a small tree">
    <defs>
      <linearGradient id="ring" x1="0" y1="0" x2="1" y2="1"><stop offset="0" stop-color="#0054AA"/><stop offset="1" stop-color="#00A9DD"/></linearGradient>
      <radialGradient id="coinPhoto"><stop offset="0" stop-color="#b7b56a"/><stop offset="1" stop-color="#7a8a5a"/></radialGradient>
    </defs>
    <circle cx="190" cy="190" r="188" fill="url(#ring)"/>
    <circle cx="198" cy="194" r="170" fill="#fff"/>
    <circle cx="198" cy="194" r="164" fill="url(#coinPhoto)"/>
  </svg>
  <svg class="abs" style="left:470px;top:150px" width="130" height="360" viewBox="0 0 130 360" aria-hidden="true">
    <path d="M20 8C80 60 110 120 95 180C85 240 70 300 20 350" stroke="#8a94a0" stroke-width="1.4" stroke-dasharray="2 4" fill="none"/>
    <circle cx="20" cy="8" r="3.5" fill="#3a4250"/><circle cx="20" cy="350" r="3.5" fill="#3a4250"/>
  </svg>
  <div class="pillar-icon" style="left:492px;top:168px"><span style="background:var(--navy)"><svg width="28" height="28" viewBox="0 0 24 24"><circle cx="8" cy="8" r="3" fill="#fff"/><circle cx="16" cy="8" r="3" fill="#fff"/><path d="M2 19c0-3 3-5 6-5s6 2 6 5M10 19c0-3 3-5 6-5s6 2 6 5" stroke="#fff" stroke-width="1.8" fill="none"/></svg></span></div>
  <div class="pillar-icon" style="left:519px;top:283px"><span style="background:var(--sky)"><svg width="26" height="26" viewBox="0 0 24 24"><path d="M12 3l2.6 5.4 5.9.8-4.3 4.1 1 5.8L12 16.3 6.8 19.1l1-5.8L3.5 9.2l5.9-.8z" fill="#fff"/></svg></span></div>
  <div class="pillar-icon" style="left:492px;top:398px"><span style="background:var(--cyan)"><svg width="28" height="28" viewBox="0 0 24 24"><rect x="3" y="4" width="18" height="12" rx="1.5" fill="none" stroke="#fff" stroke-width="1.8"/><path d="M8 20h8M12 16v4M7 12l3-3 3 2 4-4" stroke="#fff" stroke-width="1.8" fill="none"/></svg></span></div>
  <div class="pillar" style="left:592px;top:162px"><h3>THE PEOPLE</h3><p>Lorem ipsum dolor sit amet, consectetur adipiscing elit, sed do eiusmod tempor incididunt ut labore et dolore magna enim ad minim veniamea.</p></div>
  <div class="pillar" style="left:625px;top:277px"><h3>THE CUSTOMER EXPERIENCE</h3><p>Lorem ipsum dolor sit amet, consectetur adipiscing elit, sed do eiusmod tempor incididunt ut labore et dolore magna enim ad minim veniamea.</p></div>
  <div class="pillar" style="left:592px;top:392px"><h3>THE OPERATING PLATFORM</h3><p>Lorem ipsum dolor sit amet, consectetur adipiscing elit, sed do eiusmod tempor incididunt ut labore et dolore magna enim ad minim veniamea.</p></div>
  <div class="footer">
    <div class="contact"><span class="contact-icon"><svg width="12" height="12" viewBox="0 0 24 24"><path d="M6.6 10.8a15 15 0 006.6 6.6l2.2-2.2a1 1 0 011-.25 11.4 11.4 0 003.6.57 1 1 0 011 1V20a1 1 0 01-1 1A17 17 0 013 4a1 1 0 011-1h3.5a1 1 0 011 1c0 1.25.2 2.45.57 3.57a1 1 0 01-.25 1z" fill="#0054AA"/></svg></span>+1 (555) 010 2040</div>
    <div class="contact"><span class="contact-icon"><svg width="12" height="12" viewBox="0 0 24 24"><rect x="3" y="6" width="18" height="12" rx="2" fill="#0054AA"/><path d="M3 7l9 6 9-6" stroke="#fff" stroke-width="1.6" fill="none"/></svg></span>info@Altavera.com</div>
    <div class="page-no">PAGE NO 04</div>
  </div>
</section>

<!-- Slide 5: Areas of focus -->
<section class="slide" style="top:2716px">
  <div class="top-band"></div>
  <h2 class="slide-title">AREAS OF <b>FOCUS</b></h2>
  <div class="title-rule"></div>
  <div class="brand"><span class="brand-dot"></span>Altavera</div>
  <p class="body-copy abs" style="left:61px;top:114px;width:419px">As a dual US-Brazilian citizen (fluent in English/Spanish/Portuguese, working knowledge of French), my multicultural background has greatly contributed to my success in global roles. Outside of my professional endeavors, I am an avid traveler, wildlife photographer, certified sommelier, and pop culture enthusiast.</p>
  <ul class="bullets focus-list abs" style="left:61px;top:244px;width:380px">
    <li>Scaling global business operations</li>
    <li>Customer Experience</li>
    <li>Global Change Management</li>
    <li>Digital and technology transformation (emerging technologies/AI integration</li>
    <li>Business model optimization (evolved selling models)</li>
    <li>Enterprise Risk Management</li>
    <li>Changing regulatory environment (personal data use/disclosure)</li>
    <li>Talent development and succession planning</li>
    <li>ESG/Diversity</li>
  </ul>
  <svg class="photo" style="left:524px;top:130px" width="464" height="378" viewBox="0 0 464 378" role="img" aria-label="Photo of a presenter at a whiteboard leading a team meeting">
    <defs><linearGradient id="meetPhoto" x1="0" y1="0" x2="0" y2="1"><stop offset="0" stop-color="#b9d4d6"/><stop offset="1" stop-color="#e6e6e4"/></linearGradient></defs>
    <rect width="464" height="378" fill="url(#meetPhoto)"/>
  </svg>
  <div class="footer">
    <div class="contact"><span class="contact-icon"><svg width="12" height="12" viewBox="0 0 24 24"><path d="M6.6 10.8a15 15 0 006.6 6.6l2.2-2.2a1 1 0 011-.25 11.4 11.4 0 003.6.57 1 1 0 011 1V20a1 1 0 01-1 1A17 17 0 013 4a1 1 0 011-1h3.5a1 1 0 011 1c0 1.25.2 2.45.57 3.57a1 1 0 01-.25 1z" fill="#0054AA"/></svg></span>+1 (555) 010 2040</div>
    <div class="contact"><span class="contact-icon"><svg width="12" height="12" viewBox="0 0 24 24"><rect x="3" y="6" width="18" height="12" rx="2" fill="#0054AA"/><path d="M3 7l9 6 9-6" stroke="#fff" stroke-width="1.6" fill="none"/></svg></span>info@Altavera.com</div>
    <div class="page-no">PAGE NO 05</div>
  </div>
</section>

<!-- Slide 6: Benefits -->
<section class="slide" style="top:3374px">
  <div class="top-band"></div>
  <h2 class="slide-title">OUR <b>BENEFITS</b></h2>
  <div class="title-rule"></div>
  <div class="brand"><span class="brand-dot"></span>Altavera</div>
  <article class="card" style="left:102px">
    <div class="card-icon"><svg width="32" height="32" viewBox="0 0 24 24"><path d="M7 11v9H3v-9zM9 20h8.5a2 2 0 002-1.6l1.2-6A2 2 0 0018.7 10H14l.8-4a1.6 1.6 0 00-3-1L9 11z" fill="#fff"/></svg></div>
    <h3>LOREM IPSUM DOLOR</h3>
    <p>Lorem ipsum dolor sit amet, consect etur adipiscing elit, sed do eiusmod tempor incididunt ut labore et dolore magna enim ad minim veniamea. Adipiscing elit, sed do eiusmod tempor incididuntea.</p>
  </article>
  <article class="card" style="left:398px">
    <div class="card-icon"><svg width="32" height="32" viewBox="0 0 24 24"><circle cx="8" cy="8" r="3" fill="#fff"/><circle cx="16" cy="8" r="3" fill="#fff"/><path d="M2 19c0-3 3-5 6-5s6 2 6 5M10 19c0-3 3-5 6-5s6 2 6 5" stroke="#fff" stroke-width="1.8" fill="none"/></svg></div>
    <h3>LOREM IPSUM DOLOR</h3>
    <p>Lorem ipsum dolor sit amet, consect etur adipiscing elit, sed do eiusmod tempor incididunt ut labore et dolore magna enim ad minim veniamea. Adipiscing elit, sed do eiusmod tempor incididuntea.</p>
  </article>
  <article class="card" style="left:694px">
    <div class="card-icon"><svg width="32" height="32" viewBox="0 0 24 24"><circle cx="12" cy="12" r="6.5" fill="none" stroke="#fff" stroke-width="3" stroke-dasharray="3 2.1"/><circle cx="12" cy="12" r="4" fill="none" stroke="#fff" stroke-width="2"/></svg></div>
    <h3>LOREM IPSUM DOLOR</h3>
    <p>Lorem ipsum dolor sit amet, consect etur adipiscing elit, sed do eiusmod tempor incididunt ut labore et dolore magna enim ad minim veniamea. Adipiscing elit, sed do eiusmod tempor incididuntea.</p>
  </article>
  <div class="footer">
    <div class="contact"><span class="contact-icon"><svg width="12" height="12" viewBox="0 0 24 24"><path d="M6.6 10.8a15 15 0 006.6 6.6l2.2-2.2a1 1 0 011-.25 11.4 11.4 0 003.6.57 1 1 0 011 1V20a1 1 0 01-1 1A17 17 0 013 4a1 1 0 011-1h3.5a1 1 0 011 1c0 1.25.2 2.45.57 3.57a1 1 0 01-.25 1z" fill="#0054AA"/></svg></span>+1 (555) 010 2040</div>
    <div class="contact"><span class="contact-icon"><svg width="12" height="12" viewBox="0 0 24 24"><rect x="3" y="6" width="18" height="12" rx="2" fill="#0054AA"/><path d="M3 7l9 6 9-6" stroke="#fff" stroke-width="1.6" fill="none"/></svg></span>info@Altavera.com</div>
    <div class="page-no">PAGE NO 06</div>
  </div>
</section>

</body>
</html>
```